Blue Harbor Business Cards

Name Tomas Welbridge
Title Mortgage Originator
Phone (800) 614-2290 x32
Direct (571) 362-0471
Email twelbridge@blueharborhomeloans.com
NMLS #1847362
Name Lena Ortiz
Title Mortgage Originator
Location (800) 614-2290 x55
Direct (440) 276-5190
Email lortiz@blueharborhomeloans.com
NMLS #2739418
Name Desmond Holloway-Finch
Title Mortgage Originator
Location (800) 614-2290 x56
Direct (202) 634-1975
Email dhollowayfinch@blueharborhomeloans.com
NMLS #2784530
Name Rosalyn Whitaker
Title Mortgage Originator
Location (800) 614-2290 x57
Direct (240) 358-6621
Email rwhitaker@blueharborhomeloans.com
NMLS #2491086
Name Gwen Holbrook
Title Mortgage Originator
Location (800) 614-2290 x58
Direct (540) 716-2384
Email gholbrook@blueharborhomeloans.com
NMLS #2438617
Name Ravi Dunmore
Title Mortgage Originator
Location (800) 614-2290 x59
Direct (240) 563-8827
Email rdunmore@blueharborhomeloans.com
NMLS #2597142
Name Ivy Marlow
Title Mortgage Originator
Location (800) 614-2290 x60
Direct (202) 479-3306
Email ivy@ivyfindshomes.com
NMLS #2718394
Contact Information for Business Card
Name Tomas Welbridge Title Mortgage Originator Phone (800) 614-2290 x32 Direct (571) 362-0471 Email twelbridge@blueharborhomeloans.com NMLS #1847362 Name Lena Ortiz Title Mortgage Originator Location (800) 614-2290 x55 Direct (440) 276-5190 Email lortiz@blueharborhomeloans.com NMLS #2739418 Name Desmond Holloway-Finch Title Mortgage Originator Location (800) 614-2290 x56 Direct (202) 634-1975 Email dhollowayfinch@blueharborhomeloans.com NMLS #2784530 Name Rosalyn Whitaker Title Mortgage Originator Location (800) 614-2290 x57 Direct (240) 358-6621 Email rwhitaker@blueharborhomeloans.com NMLS #2491086 Name Gwen Holbrook Title Mortgage Originator Location (800) 614-2290 x58 Direct (540) 716-2384 Email gholbrook@blueharborhomeloans.com NMLS #2438617 Name Ravi Dunmore Title Mortgage Originator Location (800) 614-2290 x59 Direct (240) 563-8827 Email rdunmore@blueharborhomeloans.com NMLS #2597142 Name Ivy Marlow Title Mortgage Originator Location (800) 614-2290 x60 Direct (202) 479-3306 Email ivy@ivyfindshomes.com NMLS #2718394
Look and feel
Each slider illustrates characteristics of the customer's brand and the style your logo design should communicate.

```html
<!DOCTYPE html>
<html lang="en">
<head>
<meta charset="utf-8">
<title>Blue Harbor Business Cards</title>
<link rel="stylesheet" href="https://fonts.googleapis.com/css2?family=Poppins:wght@400;700&family=Noto+Serif:ital@1&display=swap">
<style>
  :root {
    --navy: #1b3a5a;
    --ink: #111111;
    --white: #ffffff;
    --shade: #9c9c9c;
    --backdrop: #e8e3db;
  }
  * { margin: 0; padding: 0; box-sizing: border-box; }
  html, body { width: 1200px; height: 861px; overflow: hidden; }
  body { background: var(--backdrop); position: relative; font-family: "Poppins", sans-serif; }

  .card {
    position: absolute;
    top: 168px;
    width: 313px;
    height: 547px;
    background: var(--navy);
    overflow: hidden;
    box-shadow: 0 4px 14px rgba(0,0,0,.25);
  }
  .card--lena { left: 91px; }
  .card--desmond { left: 443px; }
  .card--ravi { left: 796px; }

  .card__art { position: absolute; inset: 0; width: 100%; height: 100%; }

  .card__info { position: absolute; left: 33px; top: 272px; right: 8px; }
  .card__name {
    font-weight: 700;
    font-size: 21px;
    line-height: 1.1;
    color: var(--navy);
    text-transform: uppercase;
    white-space: nowrap;
  }
  .card__name--long { font-size: 16.5px; line-height: 23px; }
  .card__title {
    font-family: "Noto Serif", serif;
    font-style: italic;
    font-size: 14.5px;
    color: var(--ink);
    margin-top: 1px;
  }
  .contact { list-style: none; margin-top: 16px; }
  .contact__item {
    display: flex;
    align-items: center;
    gap: 7px;
    font-size: 14.5px;
    line-height: 21.5px;
    color: var(--ink);
    white-space: nowrap;
  }
  .contact__item--email { font-size: 11.2px; }
  .contact__icon { width: 13px; height: 13px; flex: none; fill: var(--navy); }
  .card__nmls { font-size: 13.5px; color: var(--ink); margin-top: 15px; }
</style>
</head>
<body>

<svg width="0" height="0" style="position:absolute">
  <defs>
    <symbol id="icon-phone" viewBox="0 0 16 16"><path d="M2 6c0-3 3-4 6-4s6 1 6 4h-3l-1-2H6L5 6zM3 7h10l1 6H2z"/><circle cx="8" cy="10" r="1.6" fill="#fff"/></symbol>
    <symbol id="icon-mobile" viewBox="0 0 16 16"><path d="M4 1h8v14H4zM5.6 2.6v10.4h4.8V2.6z"/></symbol>
    <symbol id="icon-mail" viewBox="0 0 16 16"><path d="M1 3h14v10H1zM2.5 4.2 8 8.5l5.5-4.3zM2.3 5.5v6.3l4-3.2zm11.4 0-4 3.1 4 3.2z"/></symbol>
    <symbol id="card-shapes" viewBox="0 0 534 934">
      <path d="M0 292 Q160 45 534 94 L534 742 Q330 930 0 872 Z" fill="#9c9c9c"/>
      <path d="M0 305 Q160 60 534 108 L534 723 Q330 905 0 834 Z" fill="#ffffff"/>
      <path d="M0 348 Q170 100 534 160" fill="none" stroke="#111" stroke-width="22"/>
      <path d="M0 382 Q175 138 534 194" fill="none" stroke="#111" stroke-width="7"/>
      <circle cx="352" cy="210" r="153" fill="#111"/>
    </symbol>
  </defs>
</svg>

<article class="card card--lena">
  <svg class="card__art" viewBox="0 0 534 934" preserveAspectRatio="none">
    <defs><linearGradient id="photo-lena" x1="0" y1="0" x2="0" y2="1"><stop offset="0" stop-color="#b9a48c"/><stop offset="1" stop-color="#2b3a52"/></linearGradient></defs>
    <use href="#card-shapes"/>
    <circle cx="352" cy="210" r="140" fill="url(#photo-lena)" role="img" aria-label="Portrait photo of Lena Ortiz"/>
  </svg>
  <div class="card__info">
    <h2 class="card__name">Lena Ortiz</h2>
    <p class="card__title">Mortgage Originator</p>
    <ul class="contact">
      <li class="contact__item"><svg class="contact__icon"><use href="#icon-phone"/></svg>(800) 614-2290 x55</li>
      <li class="contact__item"><svg class="contact__icon"><use href="#icon-mobile"/></svg>(440) 276-5190</li>
      <li class="contact__item contact__item--email"><svg class="contact__icon"><use href="#icon-mail"/></svg>lortiz@blueharborhomeloans.com</li>
    </ul>
    <p class="card__nmls">NMLS #2739418</p>
  </div>
</article>

<article class="card card--desmond">
  <svg class="card__art" viewBox="0 0 534 934" preserveAspectRatio="none">
    <defs><linearGradient id="photo-desmond" x1="0" y1="0" x2="0" y2="1"><stop offset="0" stop-color="#3e5272"/><stop offset="1" stop-color="#4a2c34"/></linearGradient></defs>
    <use href="#card-shapes"/>
    <circle cx="352" cy="210" r="140" fill="url(#photo-desmond)" role="img" aria-label="Portrait photo of Desmond Holloway-Finch"/>
  </svg>
  <div class="card__info">
    <h2 class="card__name card__name--long">Desmond Holloway-Finch</h2>
    <p class="card__title">Mortgage Originator</p>
    <ul class="contact">
      <li class="contact__item"><svg class="contact__icon"><use href="#icon-phone"/></svg>(800) 614-2290 x56</li>
      <li class="contact__item"><svg class="contact__icon"><use href="#icon-mobile"/></svg>(202) 634-1975</li>
      <li class="contact__item contact__item--email"><svg class="contact__icon"><use href="#icon-mail"/></svg>dhollowayfinch@blueharborhomeloans.com</li>
    </ul>
    <p class="card__nmls">NMLS #2784530</p>
  </div>
</article>

<article class="card card--ravi">
  <svg class="card__art" viewBox="0 0 534 934" preserveAspectRatio="none">
    <defs><linearGradient id="photo-ravi" x1="0" y1="0" x2="0" y2="1"><stop offset="0" stop-color="#d8d2c8"/><stop offset="1" stop-color="#2a3f78"/></linearGradient></defs>
    <use href="#card-shapes"/>
    <circle cx="352" cy="210" r="140" fill="url(#photo-ravi)" role="img" aria-label="Portrait photo of Ravi Dunmore"/>
  </svg>
  <div class="card__info">
    <h2 class="card__name">Ravi Dunmore</h2>
    <p class="card__title">Mortgage Originator</p>
    <ul class="contact">
      <li class="contact__item"><svg class="contact__icon"><use href="#icon-phone"/></svg>(800) 614-2290 x59</li>
      <li class="contact__item"><svg class="contact__icon"><use href="#icon-mobile"/></svg>(240) 563-8827</li>
      <li class="contact__item contact__item--email"><svg class="contact__icon"><use href="#icon-mail"/></svg>rdunmore@blueharborhomeloans.com</li>
    </ul>
    <p class="card__nmls">NMLS #2597142</p>
  </div>
</article>

</body>
</html>
```